A mobile coffee, eats and treats van. We sell freshly ground Valtorino coffee, a selection of yummy things to eats, and lovely giftwares, including candles, scarfs, jewellery. We also have an online store where additional home and giftwares can be purchased

Thanks so much for all your efforts so far, I have received some great concepts.  Just wanted to send out a reminder that our concept is coffee, eats and treats (the treats being home and gift ware)  We have a mobile van and also an online store.  I dont want to make my business card too "busy" but at the same time I would like to give my potential customers something that will really excite and intrigue them...

Reason: Its the weekend....have a break!

Thank you everyone for your designs...I think I have made a decision...have just sent out a couple of questions.  I will be loading a new project shortly if you are interested?  Thanks, Marlene

Store

The Dusky Wren - Coffee, Eats & Treats
Marlene Quistorff
0459 863 205
marlene@theduskywren.com.au
www.theduskywren.com.au
www.facebook.com/theduskywren
https://twitter.com/TheDuskyWren

• It would be good to have a rewards program on the back, we can tick off when prople buy coffee....5th coffee free...something like that...

It would also be good for the card to look like a gift tag....

```html
<!DOCTYPE html>
<html lang="en">
<head>
<meta charset="utf-8">
<title>The Dusky Wren – Business Card</title>
<link rel="stylesheet" href="https://fonts.googleapis.com/css2?family=Arimo:wght@400;700&family=Dancing+Script:wght@400&display=swap">
<style>
  :root {
    --backdrop: #1e2a2c;
    --card: #f3f2e2;
    --ink: #2c2c1a;
    --olive: #a9ad72;
    --olive-soft: #cfd1a6;
    --olive-faint: #dcdcbb;
  }
  * { box-sizing: border-box; margin: 0; padding: 0; }
  html, body {
    width: 1200px; height: 693px; overflow: hidden;
    background: var(--backdrop);
    font-family: "Arimo", Arial, sans-serif;
  }
  .stage {
    position: relative; width: 1200px; height: 693px;
    display: flex; align-items: center; justify-content: center; gap: 40px;
  }
  .card {
    position: relative; width: 540px; height: 309px;
    background: var(--card); overflow: hidden;
    box-shadow: 0 10px 30px rgba(0,0,0,.45);
  }
  /* front */
  .card-front .holder-name {
    position: absolute; top: 26px; right: 30px;
    font-size: 27px; font-weight: 700; color: var(--ink); letter-spacing: .3px;
  }
  .card-front .van-art {
    position: absolute; left: 0; top: 86px; width: 230px; height: 130px;
  }
  .card-front .brand-name {
    position: absolute; top: 82px; right: 30px;
    font-size: 36px; font-weight: 700; color: var(--olive); letter-spacing: -.5px;
  }
  .card-front .brand-tagline {
    position: absolute; top: 134px; right: 30px;
    font-size: 21px; font-weight: 700; color: var(--ink);
  }
  .contact-list {
    position: absolute; list-style: none;
    font-size: 14.5px; font-weight: 700; color: var(--ink); line-height: 1.45;
  }
  .contact-list li::before { content: "• "; }
  .contact-list.primary { left: 22px; bottom: 18px; }
  .contact-list.social { right: 22px; bottom: 96px; font-size: 13.5px; }
  /* back */
  .card-back .van-art {
    position: absolute; right: 40px; top: 14px; width: 160px; height: 80px;
  }
  .card-back .rewards {
    position: absolute; left: 28px; top: 118px; right: 24px;
    font-family: "Dancing Script", cursive; color: var(--ink);
    font-size: 24px; line-height: 1.3;
  }
  .card-back .rewards .call { display: block; font-size: 27px; }
  .card-back .rewards .offer { display: block; padding-left: 22px; }
  .card-back .brand-name {
    position: absolute; right: 26px; bottom: 22px;
    font-size: 24px; font-weight: 700; color: var(--olive);
  }
</style>
</head>
<body>
<main class="stage">
  <section class="card card-front">
    <p class="holder-name">Marlene Quistorff</p>
    <svg class="van-art" role="img" aria-label="Illustration of the coffee van" viewBox="0 0 230 130">
      <rect x="0" y="0" width="230" height="130" rx="18" fill="var(--olive-soft)"/>
    </svg>
    <p class="brand-name">The Dusky Wren</p>
    <p class="brand-tagline">Coffee, Eats &amp; Treats</p>
    <ul class="contact-list social">
      <li>https://twitter.com/TheDuskyWren</li>
      <li>www.facebook.com/theduskywren</li>
    </ul>
    <ul class="contact-list primary">
      <li>0459 863 205</li>
      <li>www.theduskywren.com.au</li>
      <li>marlene@theduskywren.com.au</li>
    </ul>
  </section>

  <section class="card card-back">
    <svg class="van-art" role="img" aria-label="Faint illustration of the coffee van" viewBox="0 0 160 80">
      <rect x="0" y="0" width="160" height="80" rx="14" fill="var(--olive-faint)"/>
    </svg>
    <p class="rewards">
      <span class="call">Invite everyone!!</span>
      <span class="offer">“Just buy a coffee if you have 4 friends with you and the 5th one will be free.”</span>
    </p>
    <p class="brand-name">The Dusky Wren</p>
  </section>
</main>
</body>
</html>
```